CBD AgriBusiness Cannabis Cup Business Card

We are HiTec producer of medical cannabis CBD Switzerland of high quality. Our website is alpinleafo.com, we will also revisit it graphically, the winner of this contest will be the graphic designer chosen for the new design of the website. We stand out by the skill of the team, many of our engineers we win cup cannabis. I join the current map to take as an example but to revisit completely: deletion of surname and first name, modification of funds (front / back), reorganization of text info, highlighting the address of the website. three characteristics define the business card: Professional, Class, refined. The business card must be optimized for soft-touch and selective varnish printing.

Target Market(s)

Customers and Suppliers

Industry/Entity Type

Agribusiness

Contact Information for Business Card

Logo, Tél / Whatsapp, mail, url du site : alpinleafo.com

Font styles to use
Sans Serif

Requirements
Must have
• Logo of alpinleafo.com
Nice to have
• a design that stands out well on the selective varnish
Should not have
• Last name and first name

```html
<!DOCTYPE html>
<html lang="en">
<head>
<meta charset="utf-8">
<title>alpinleafo – business card</title>
<link href="https://fonts.googleapis.com/css2?family=Roboto:wght@400;500;700&display=swap" rel="stylesheet">
<style>
  :root {
    --backdrop: #1d1d1f;
    --card: #303033;
    --green: #86c14f;
    --logo-grey: #58585c;
    --text-light: #e6e6e6;
    --white: #ffffff;
  }
  * { margin: 0; padding: 0; box-sizing: border-box; }
  html, body {
    width: 1200px; height: 800px; overflow: hidden;
    background: var(--backdrop);
    font-family: "Roboto", Arial, sans-serif;
  }
  .stage {
    position: relative; width: 1200px; height: 800px;
  }
  .card {
    position: absolute; left: 320px;
    width: 560px; height: 320px;
    background: var(--card);
    box-shadow: 0 18px 40px rgba(0,0,0,.55);
    overflow: hidden;
  }
  .card--front { top: 50px; }
  .card--back { top: 430px; }

  .logo {
    position: absolute; display: flex; align-items: center; gap: 10px;
  }
  .logo__square {
    width: 20px; height: 20px; background: var(--green);
  }
  .logo__name {
    font-weight: 700; font-size: 44px; letter-spacing: -1px;
    color: var(--logo-grey); line-height: 1;
  }
  .card--front .logo { left: 168px; top: 110px; }
  .card--back .logo { left: 52px; top: 88px; }
  .card--back .logo__name { font-size: 40px; }

  .front-band {
    position: absolute; left: 0; right: 0; top: 190px; height: 46px;
    background: var(--green);
    display: flex; align-items: center; justify-content: center;
  }
  .front-band__tagline {
    color: var(--white); font-weight: 500; font-size: 15px;
    letter-spacing: 4px; text-transform: uppercase;
  }

  .contacts {
    position: absolute; left: 56px; top: 160px;
    list-style: none;
  }
  .contacts__item {
    font-size: 14px; color: var(--text-light); line-height: 24px;
  }
  .contacts__label {
    color: var(--green); font-weight: 700; letter-spacing: 1.5px;
    margin-right: 6px;
  }
  .contacts__item:nth-child(2) { padding-left: 10px; }
  .contacts__item:nth-child(3) { padding-left: 20px; }

  .back-block {
    position: absolute; top: 250px; height: 34px; background: var(--green);
  }
  .back-block--short { left: 0; width: 108px; }
  .back-block--url {
    left: 118px; right: 0;
    display: flex; align-items: center; justify-content: flex-end;
    gap: 12px; padding-right: 56px;
  }
  .back-block__url {
    color: var(--white); font-weight: 700; font-size: 17px; letter-spacing: 2px;
  }
  .globe { width: 16px; height: 16px; }
</style>
</head>
<body>
<main class="stage">
  <section class="card card--front" aria-label="Card front">
    <div class="logo">
      <span class="logo__square"></span>
      <span class="logo__name">alpinleafo</span>
    </div>
    <div class="front-band">
      <span class="front-band__tagline">Alpine Leaf Growers</span>
    </div>
  </section>

  <section class="card card--back" aria-label="Card back">
    <div class="logo">
      <span class="logo__square"></span>
      <span class="logo__name">alpinleafo</span>
    </div>
    <ul class="contacts">
      <li class="contacts__item"><span class="contacts__label">Tel.</span>+41 (0) 79 314 52 67</li>
      <li class="contacts__item"><span class="contacts__label">Sales :</span>sales@alpinleafo.com</li>
      <li class="contacts__item"><span class="contacts__label">Contact :</span>office@alpinleafo.com</li>
    </ul>
    <div class="back-block back-block--short"></div>
    <div class="back-block back-block--url">
      <svg class="globe" viewBox="0 0 16 16" aria-hidden="true">
        <g fill="none" stroke="#ffffff" stroke-width="1.3">
          <circle cx="8" cy="8" r="6.5"/>
          <ellipse cx="8" cy="8" rx="3" ry="6.5"/>
          <line x1="1.5" y1="8" x2="14.5" y2="8"/>
          <line x1="2.6" y1="4.6" x2="13.4" y2="4.6"/>
          <line x1="2.6" y1="11.4" x2="13.4" y2="11.4"/>
        </g>
      </svg>
      <span class="back-block__url">www.alpinleafo.com</span>
    </div>
  </section>
</main>
</body>
</html>
```